Financial Services Compliance Specialist needs a brochure

I need a business brochure that aligns to the theme of my stationery. My website is www.tpwlconsulting.com.au. I require a menu of services. The brochure needs to be A5 and PDF format so I can email it. I have attached a file with the wording and some suggested photos. I need a lot of help with format so please ignore the format in the attachment. A winner has already been selected.

Target Market(s)

Australian Financial Services Licensees

Industry/Entity Type

Business

Font styles to use
Sans Serif

Colors
ecf6fa
3176b5
0493ce

Requirements
Must have
• Photos of people
Nice to have
• 8 pages maximum

```html
<!DOCTYPE html>
<html lang="en">
<head>
<meta charset="utf-8">
<title>TPWL Consulting – Licensee Services Brochure</title>
<link rel="stylesheet" href="https://fonts.googleapis.com/css2?family=Didact+Gothic&family=Montserrat:wght@600&display=swap">
<style>
  :root {
    --pale: #ecf6fa;
    --blue: #3176b5;
    --sky: #0493ce;
    --mid: #3a8ad0;
    --navy: #1b3a63;
    --ink: #1d2430;
    --white: #ffffff;
    --stage: #e4e7ea;
  }
  * { box-sizing: border-box; margin: 0; padding: 0; }
  html, body { width: 1200px; height: 888px; overflow: hidden; }
  body {
    background: var(--stage);
    font-family: "Didact Gothic", "Century Gothic", sans-serif;
    position: relative;
  }
  .page {
    position: absolute;
    top: 75px;
    width: 520px;
    height: 735px;
    overflow: hidden;
    background: linear-gradient(90deg, var(--mid) 0%, #3584c8 50%, var(--blue) 100%);
    box-shadow: 0 6px 18px rgba(0,0,0,.25);
  }
  .page--cover { left: 55px; }
  .page--menu { left: 630px; }
  .page-lines {
    position: absolute; inset: 0; width: 520px; height: 735px;
    pointer-events: none;
  }

  /* Cover */
  .cover-header {
    position: absolute; inset: 0 0 auto 0; height: 125px;
    background: linear-gradient(180deg, #ffffff, #eceef0);
    display: flex; align-items: center;
  }
  .brand {
    width: 228px; padding-left: 14px;
    display: flex; align-items: center; gap: 9px;
    color: var(--blue); font-size: 31px; line-height: 1.02;
  }
  .brand-mark { width: 14px; height: 14px; background: var(--sky); flex: none; }
  .header-divider { width: 2px; height: 78px; background: #c9cdd2; }
  .header-title { flex: 1; padding-right: 14px; text-align: right; }
  .header-title .kicker {
    font-family: "Montserrat", sans-serif; font-weight: 600;
    color: var(--sky); font-size: 22px; letter-spacing: .2px;
  }
  .header-title .sub { color: var(--ink); font-size: 24.5px; margin-top: 3px; }
  .cover-photo {
    position: absolute; top: 125px; left: 0; width: 520px; height: 340px;
    clip-path: path('M0 0 H520 V255 Q280 345 0 295 Z');
    background:
      radial-gradient(ellipse 120px 170px at 30% 40%, rgba(150,190,230,.55), transparent 70%),
      radial-gradient(ellipse 200px 150px at 78% 52%, rgba(40,170,245,.95), transparent 72%),
      linear-gradient(90deg, #232b36 0%, #37414f 28%, #2c3a4c 45%, #124a82 62%, #0c3767 100%);
  }
  .cover-title {
    position: absolute; top: 515px; width: 100%; text-align: center;
    color: var(--ink); font-size: 42px; font-weight: 400; letter-spacing: 1px;
  }
  .cover-rule {
    position: absolute; top: 578px; left: 100px; width: 320px; height: 1px;
    background: rgba(255,255,255,.45);
  }
  .cover-tagline {
    position: absolute; top: 603px; width: 100%; text-align: center;
    color: var(--white); font-size: 21px; line-height: 26px; letter-spacing: .3px;
  }
  .cover-url {
    position: absolute; top: 685px; left: 98px; width: 325px; height: 50px;
    border-radius: 8px 8px 0 0;
    background: linear-gradient(180deg, #ffffff, #dfe3e7);
    color: var(--ink); font-size: 20px;
    display: flex; align-items: center; justify-content: center;
  }

  /* Menu page */
  .intro {
    position: absolute; top: 30px; left: 38px; width: 446px;
    color: var(--white); font-size: 17.5px; line-height: 20.8px;
    text-align: justify; letter-spacing: .4px;
  }
  .menu-photo {
    position: absolute; inset: 0;
    clip-path: path('M0 222 Q260 290 520 185 V548 Q280 540 0 595 Z');
    background:
      radial-gradient(ellipse 70px 90px at 92% 42%, rgba(236,200,176,.8), transparent 75%),
      radial-gradient(ellipse 60px 80px at 75% 46%, rgba(220,185,165,.6), transparent 75%),
      radial-gradient(ellipse 180px 140px at 88% 68%, rgba(28,36,52,.95), transparent 75%),
      linear-gradient(90deg, #ffffff 0%, #ffffff 32%, #eef3f8 46%, #d3dde8 58%, #7a8594 74%, #3a4556 88%, #242e3e 100%);
  }
  .menu-list {
    position: absolute; top: 298px; left: 40px; list-style: none;
    color: var(--ink); font-size: 17.5px;
  }
  .menu-list li { height: 29.2px; display: flex; align-items: center; gap: 15px; }
  .menu-list svg { width: 10px; height: 12px; flex: none; }
  .imprint {
    position: absolute; top: 667px; width: 100%; text-align: center;
    color: var(--white); font-size: 20px; font-style: italic; line-height: 25px;
    letter-spacing: .3px;
  }
</style>
</head>
<body>

<section class="page page--cover">
  <header class="cover-header">
    <div class="brand"><span class="brand-mark"></span><span>TPWL<br>Consulting</span></div>
    <div class="header-divider"></div>
    <div class="header-title">
      <div class="kicker">FINANCIAL SERVICES</div>
      <div class="sub">compliance specialist</div>
    </div>
  </header>
  <div class="cover-photo" role="img" aria-label="Photo of a consultant in a dark suit writing the word Consulting over a glowing blue world map with business keywords"></div>
  <svg class="page-lines" viewBox="0 0 520 735">
    <path d="M0 424 Q280 474 520 384" fill="none" stroke="#ffffff" stroke-width="9"/>
    <path d="M0 436 Q280 522 520 452" fill="none" stroke="#1b3a63" stroke-width="6"/>
  </svg>
  <h1 class="cover-title">Licensee Services</h1>
  <div class="cover-rule"></div>
  <p class="cover-tagline">Protecting your brand and optimising<br>the value of your business</p>
  <div class="cover-url">www.tpwlconsulting.com.au</div>
</section>

<section class="page page--menu">
  <p class="intro">TPWL Consulting provides a range of consulting services that deliver practical and effective solutions to the many compliance challenges in your business.<br>Our compliance services include the design and delivery of tailored solutions that drive adviser efficiency and optimise performance.</p>
  <div class="menu-photo" role="img" aria-label="Photo of smiling business people working at computers in a bright office"></div>
  <svg class="page-lines" viewBox="0 0 520 735">
    <path d="M0 200 Q260 268 520 163" fill="none" stroke="#ffffff" stroke-width="8"/>
    <path d="M0 212 Q260 280 520 175" fill="none" stroke="#3176b5" stroke-width="14"/>
    <path d="M0 221 Q260 289 520 184" fill="none" stroke="#1b3a63" stroke-width="4"/>
    <path d="M0 596 Q280 541 520 549" fill="none" stroke="#1b3a63" stroke-width="5"/>
    <path d="M0 608 Q280 553 520 561" fill="none" stroke="#3176b5" stroke-width="16"/>
    <path d="M0 624 Q280 569 520 577" fill="none" stroke="#ffffff" stroke-width="10"/>
  </svg>
  <ul class="menu-list">
    <li><svg viewBox="0 0 10 12"><path d="M2 1 L8 6 L2 11" fill="none" stroke="#0493ce" stroke-width="2.4"/></svg>About Us</li>
    <li><svg viewBox="0 0 10 12"><path d="M2 1 L8 6 L2 11" fill="none" stroke="#0493ce" stroke-width="2.4"/></svg>Our Services</li>
    <li><svg viewBox="0 0 10 12"><path d="M2 1 L8 6 L2 11" fill="none" stroke="#0493ce" stroke-width="2.4"/></svg>New AFSL Licensee Packages</li>
    <li><svg viewBox="0 0 10 12"><path d="M2 1 L8 6 L2 11" fill="none" stroke="#0493ce" stroke-width="2.4"/></svg>Licensee &amp; Adviser Reviews</li>
    <li><svg viewBox="0 0 10 12"><path d="M2 1 L8 6 L2 11" fill="none" stroke="#0493ce" stroke-width="2.4"/></svg>Complaints &amp; Breach Management</li>
    <li><svg viewBox="0 0 10 12"><path d="M2 1 L8 6 L2 11" fill="none" stroke="#0493ce" stroke-width="2.4"/></svg>Consulting Services</li>
    <li><svg viewBox="0 0 10 12"><path d="M2 1 L8 6 L2 11" fill="none" stroke="#0493ce" stroke-width="2.4"/></svg>Contact us</li>
  </ul>
  <p class="imprint">TPWL Consulting Pty Ltd&nbsp; ABN 51<br>302 417 655</p>
</section>

</body>
</html>
```